IV Bag Graphic for IV Therapy Bar

Hello we are offering an IV Therapy Bar to our medical practice. We already have a logo would like a cool design label for the IV bag. We will utilize this label for social media advertising, a sticker for the saline bag and marketing material. Woukd like something unique, sharp, bold and professional. We signed up for the Social Media package so the design will need to hold and be creative.

Target Market(s)

25-35 yrs old

Requirements
Must have
• Velmora Clinical Research name and logo- Clear inference it is IV therapy
Nice to have
• Innovation- Lines to write Name - Also please give examples of the different IV therapies (Myers cocktail) etc (screenshot example of therapies is attached)
Should not have
• In the attached examples the packaging and label are black, in open.

```html
<!DOCTYPE html>
<html lang="en">
<head>
<meta charset="utf-8">
<title>Weight Loss Wellness Drip – IV Bag Labels</title>
<link rel="stylesheet" href="https://fonts.googleapis.com/css2?family=Bebas+Neue&family=Quicksand:wght@400;500;700&display=swap">
<style>
  :root {
    --bg-light: #ffffff;
    --bg-dark: #8fa6b6;
    --bag-light: #e9f0f3;
    --bag-mid: #c9d8df;
    --bag-fruit: #7f9a6a;
    --label-charcoal: #474747;
    --label-magenta: #e03ae8;
    --label-border: #ffffff;
    --ink: #ffffff;
  }
  * { margin: 0; padding: 0; box-sizing: border-box; }
  html, body { width: 1182px; height: 1200px; overflow: hidden; }
  body {
    position: relative;
    background: linear-gradient(135deg, var(--bg-light) 0%, #dfe7ec 45%, var(--bg-dark) 100%);
    font-family: "Quicksand", sans-serif;
    color: var(--ink);
  }
  .iv-bag { position: absolute; top: 25px; width: 520px; height: 1150px; }
  .iv-bag--left { left: 52px; }
  .iv-bag--right { left: 611px; }

  .drip-label {
    position: absolute;
    top: 264px;
    width: 396px;
    height: 470px;
    border: 7px solid var(--label-border);
    border-radius: 30px;
  }
  .drip-label--charcoal { left: 116px; background: var(--label-charcoal); }
  .drip-label--magenta { left: 677px; background: var(--label-magenta); }

  .drip-label__icon { position: absolute; left: 137px; top: 15px; width: 130px; height: 94px; }
  .drip-label__title {
    position: absolute; left: 0; right: 0; top: 118px;
    text-align: center;
    font-family: "Bebas Neue", sans-serif;
    font-size: 66px; line-height: 1; letter-spacing: 0.5px;
  }
  .drip-label__rule {
    position: absolute; left: 39px; top: 186px; width: 302px; height: 2px;
    background: var(--ink);
  }
  .drip-label__subtitle {
    position: absolute; left: 0; right: 0; top: 196px;
    text-align: center;
    font-size: 38px; font-weight: 500; line-height: 1;
  }
  .drip-label__ingredients {
    position: absolute; left: 30px; top: 253px;
    list-style: none;
    font-size: 15px; font-weight: 400; letter-spacing: 1.2px;
    line-height: 26.7px;
  }
  .drip-label__ingredients li::before {
    content: ""; display: inline-block;
    width: 7px; height: 7px; border-radius: 50%;
    background: var(--ink);
    margin-right: 8px; vertical-align: 2px;
  }
  .drip-label__volume {
    position: absolute; left: 164px; top: 413px;
    font-size: 14px; font-weight: 500; line-height: 26.7px;
  }
  .drip-label__brand {
    position: absolute; left: 262px; top: 350px; width: 110px;
    text-align: center;
    font-size: 11px; font-weight: 700; line-height: 1.2; letter-spacing: 0.3px;
    text-transform: uppercase;
  }
  .drip-label__brand-dot {
    display: block; width: 38px; height: 38px; margin: 0 auto 8px;
    border-radius: 50%; border: 3px solid var(--ink);
  }
</style>
</head>
<body>

  <svg class="iv-bag iv-bag--left" viewBox="0 0 520 1150" role="img" aria-label="Clear IV saline bag with kiwi, orange and blueberry slices inside">
    <defs>
      <linearGradient id="bagFillLeft" x1="0" y1="0" x2="0" y2="1">
        <stop offset="0" stop-color="#e9f0f3"/>
        <stop offset="0.6" stop-color="#c9d8df"/>
        <stop offset="0.78" stop-color="#8fa07e"/>
        <stop offset="0.9" stop-color="#dfe8ec"/>
      </linearGradient>
    </defs>
    <path d="M20 10 Q260 40 500 10 L512 150 L505 870 L515 960 L10 960 L18 870 L12 150 Z" fill="url(#bagFillLeft)"/>
    <rect x="195" y="960" width="38" height="180" rx="10" fill="#dfe8ec"/>
    <rect x="300" y="960" width="38" height="180" rx="10" fill="#dfe8ec"/>
  </svg>

  <svg class="iv-bag iv-bag--right" viewBox="0 0 520 1150" role="img" aria-label="Clear IV saline bag with kiwi, orange and blueberry slices inside">
    <defs>
      <linearGradient id="bagFillRight" x1="0" y1="0" x2="0" y2="1">
        <stop offset="0" stop-color="#e9f0f3"/>
        <stop offset="0.6" stop-color="#c9d8df"/>
        <stop offset="0.78" stop-color="#8fa07e"/>
        <stop offset="0.9" stop-color="#dfe8ec"/>
      </linearGradient>
    </defs>
    <path d="M20 10 Q260 40 500 10 L512 150 L505 870 L515 960 L10 960 L18 870 L12 150 Z" fill="url(#bagFillRight)"/>
    <rect x="195" y="960" width="38" height="180" rx="10" fill="#dfe8ec"/>
    <rect x="300" y="960" width="38" height="180" rx="10" fill="#dfe8ec"/>
  </svg>

  <section class="drip-label drip-label--charcoal">
    <svg class="drip-label__icon" viewBox="0 0 130 94" fill="none" stroke="#fff" stroke-width="4" stroke-linecap="round" stroke-linejoin="round" aria-hidden="true">
      <rect x="3" y="3" width="88" height="86" rx="10"/>
      <rect x="13" y="12" width="68" height="24" rx="5"/>
      <line x1="47" y1="32" x2="38" y2="22"/>
      <ellipse cx="34" cy="62" rx="9" ry="15"/>
      <ellipse cx="60" cy="62" rx="9" ry="15"/>
      <line x1="114" y1="16" x2="114" y2="58"/>
      <polyline points="102,47 114,60 126,47"/>
    </svg>
    <h1 class="drip-label__title">Weight Loss</h1>
    <div class="drip-label__rule"></div>
    <h2 class="drip-label__subtitle">WELLNESS DRIP</h2>
    <ul class="drip-label__ingredients">
      <li>B-COMPLEX VITAMIN</li>
      <li>VITAMIN B12</li>
      <li>L-ARGININE</li>
      <li>L-CARNITINE</li>
      <li>L GLUTAMINE</li>
      <li>TAURINE</li>
      <li>MIC</li>
    </ul>
    <p class="drip-label__volume">1000 ML</p>
    <div class="drip-label__brand"><span class="drip-label__brand-dot"></span>Velmora<br>Clinical Research</div>
  </section>

  <section class="drip-label drip-label--magenta">
    <svg class="drip-label__icon" viewBox="0 0 130 94" fill="none" stroke="#fff" stroke-width="4" stroke-linecap="round" stroke-linejoin="round" aria-hidden="true">
      <rect x="3" y="3" width="88" height="86" rx="10"/>
      <rect x="13" y="12" width="68" height="24" rx="5"/>
      <line x1="47" y1="32" x2="38" y2="22"/>
      <ellipse cx="34" cy="62" rx="9" ry="15"/>
      <ellipse cx="60" cy="62" rx="9" ry="15"/>
      <line x1="114" y1="16" x2="114" y2="58"/>
      <polyline points="102,47 114,60 126,47"/>
    </svg>
    <h1 class="drip-label__title">Weight Loss</h1>
    <div class="drip-label__rule"></div>
    <h2 class="drip-label__subtitle">WELLNESS DRIP</h2>
    <ul class="drip-label__ingredients">
      <li>B-COMPLEX VITAMIN</li>
      <li>VITAMIN B12</li>
      <li>L-ARGININE</li>
      <li>L-CARNITINE</li>
      <li>L GLUTAMINE</li>
      <li>TAURINE</li>
      <li>MIC</li>
    </ul>
    <p class="drip-label__volume">1000 ML</p>
    <div class="drip-label__brand"><span class="drip-label__brand-dot"></span>Velmora<br>Clinical Research</div>
  </section>

</body>
</html>
```